automatic Real Estate Sales Brochure

Print-out of 3 to 8 pages automatically on a color inkjet printer. Page size A4
All details for my Real Estate Sales Design Project are in attached file.
Here some points:
We have abound 100 real estate objects for sale (houses, flats and pieces of land).
For each item, our system creates automatically a sales documentation, which we print out and hand to the potential buyers after they've visited the object or send it by mail upon request in form of a pdf.
This document should be of 3 to maximum 8 pages.
It should be of a modern design and invite the client to read it.
The information should be clear and quick to find.
If the global look could somehow relate to the look of our web site www.norvelhaus.ch, that would be nice.
The company data is there for legal reasons, but it is the agent's phone and mail that the clients should use for contact.
The photos should be of big size (2 by page?) without being distorted nor cut.
Optionally, to save ink and pages, maybe only the first 3-4 photos full size and the rest smaller?

Target Market(s)

will be printed or sent as PDF "on the fly", meaning no pre-printing at a print shop!

Industry/Entity Type

Real Estate

Font styles to use
Sans Serif

Requirements
Must have
• see details in attached file
Should not have
• no edge-to-edge printing
• no double-page printing (A3)

```html
<!DOCTYPE html>
<html lang="fr">
<head>
<meta charset="utf-8">
<title>Lumineux 4.5 – Brochure de vente</title>
<link href="https://fonts.googleapis.com/css2?family=Montserrat:wght@700;800&family=Source+Sans+3:wght@400;600;700&display=swap" rel="stylesheet">
<style>
:root{
  --red:#e95c57;
  --red-soft:#f06b64;
  --grey-label:#c9c9c9;
  --grey-value:#dcdcdc;
  --grey-box:#d3d3d3;
  --ink:#1d1d1d;
  --white:#ffffff;
  --desk:#e6e6e6;
}
*{margin:0;padding:0;box-sizing:border-box}
html,body{width:1200px;height:852px;overflow:hidden;background:var(--desk)}
body{font-family:"Source Sans 3",Arial,sans-serif;color:var(--ink)}
.spread{position:relative;width:1200px;height:852px}
.page{position:absolute;top:12px;width:576px;height:828px;background:var(--white);overflow:hidden;box-shadow:0 1px 4px rgba(0,0,0,.15)}
.page-one{left:12px}
.page-two{left:612px}
.abs{position:absolute}

/* page one */
.photo-balcony{left:14px;top:14px;width:548px;height:408px;
  background:linear-gradient(180deg,#cfe0ef 0%,#dfe6d8 22%,#8fa36a 45%,#c9b28f 70%,#e9d2b4 100%)}
.accent-strip{left:14px;top:412px;width:548px;height:20px}
.brand-ribbon{left:130px;top:388px;width:316px;height:62px}
.brand-name{left:130px;top:401px;width:316px;text-align:center;font-weight:700;font-size:28px;line-height:36px;color:var(--red);letter-spacing:.5px}

.facts{left:14px;top:492px;width:356px;border-collapse:collapse;font-size:12.5px;line-height:1.2}
.facts td{height:54px;text-align:center;vertical-align:middle;border-bottom:2px solid var(--red-soft);padding:0 4px}
.facts tr:last-child td{border-bottom:none}
.facts .label{background:var(--grey-label);font-weight:700;width:96px}
.facts .value{background:var(--grey-value);width:82px}

.divider{left:384px;top:492px;width:2px;height:218px;background:var(--red-soft)}
.broker{left:396px;top:490px;width:160px;text-align:center}
.broker-title{font-size:20px;color:var(--red);line-height:1.15}
.broker-name,.broker-phone{font-size:14px;line-height:1.3}
.portrait{left:419px;top:554px;width:114px;height:156px;background:linear-gradient(180deg,#e8e2dc,#8a6a58 55%,#2a2a2a)}

/* footers */
.footer{left:14px;top:740px;width:548px;height:74px;background:var(--red);color:var(--white);font-size:12.5px}
.footer .col{position:absolute;line-height:1.35;white-space:nowrap}
.page-one .footer .col{top:14px}
.page-one .footer .contact{top:20px;font-size:13.5px}
.page-two .footer .col{top:10px}
.footer-brand{position:absolute;right:16px;top:24px;font-weight:700;font-size:22px;line-height:1}

/* page two */
.header-band{left:14px;top:14px;width:548px;height:236px}
.title-box{left:14px;top:84px;width:356px;height:58px;border:2px solid var(--white);color:var(--white);font-family:"Montserrat",Arial,sans-serif;font-weight:800;text-align:center;padding-top:6px;font-variant:small-caps}
.title-main{font-size:21px;line-height:1.1}
.title-sub{font-size:13px;line-height:1.5;padding-left:24px}

.photo-bedroom{left:20px;top:224px;width:240px;height:142px;background:linear-gradient(90deg,#2b2b2b 0 45%,#f3e5b8 60%,#c98f52 100%)}
.photo-bath{left:20px;top:370px;width:112px;height:64px;background:linear-gradient(135deg,#f2f2f2,#c9c9c9)}
.photo-kitchen{left:136px;top:370px;width:124px;height:64px;background:linear-gradient(180deg,#f4f0ea,#c8925a)}
.photo-living{left:20px;top:438px;width:240px;height:116px;background:linear-gradient(180deg,#f7f3ea 0 55%,#c68b4f 100%)}
.photo-terrace{left:266px;top:148px;width:296px;height:228px;background:linear-gradient(180deg,#cfe0f0 0%,#6f9a4a 40%,#3f5a2c 65%,#b0a79a 100%);clip-path:polygon(0 0,100% 0,100% 93%,0 100%)}
.photo-garden{left:270px;top:574px;width:292px;height:116px;background:linear-gradient(180deg,#d6e6f2 0%,#7fa253 45%,#4e7a2e 100%)}

.location-box{left:20px;top:558px;width:240px;height:152px;background:var(--grey-box);padding:11px 8px;font-size:11.2px;font-weight:700;line-height:1.3}

.intro{left:270px;top:382px;width:290px;font-size:7px;line-height:1.4;color:var(--red)}
.copy{top:428px;font-size:6.6px;line-height:1.45}
.copy p{margin-bottom:5px}
.copy-a{left:270px;width:138px}
.copy-b{left:418px;width:142px}
.price-tag{left:418px;top:520px;width:140px;height:22px;background:var(--red);color:var(--white);text-align:center;font-size:14px;line-height:22px}
.cta{left:272px;top:694px;font-size:12.5px;line-height:1.5}
.cta-name{color:var(--red);font-weight:700}
</style>
</head>
<body>
<main class="spread">

  <section class="page page-one">
    <div class="abs photo-balcony" role="img" aria-label="Photo du balcon arrondi donnant sur un jardin arboré"></div>
    <svg class="abs accent-strip" width="548" height="20" viewBox="0 0 548 20"><polygon points="0,8 548,0 548,6 0,14" fill="#e95c57"/></svg>
    <svg class="abs brand-ribbon" width="316" height="62" viewBox="0 0 316 62">
      <polygon points="0,0 316,0 304,31 316,62 0,62 12,31" fill="#c9c9c9"/>
      <polygon points="12,9 304,9 296,31 304,53 12,53 20,31" fill="#dedede"/>
    </svg>
    <div class="abs brand-name">norvelhaus</div>

    <table class="abs facts">
      <tr><td class="label">Type de Bien</td><td class="value">Appartement</td><td class="label">Prix</td><td class="value">895 000</td></tr>
      <tr><td class="label">Surface habitable m2</td><td class="value">100 m2</td><td class="label">Annee de construction</td><td class="value">1994</td></tr>
      <tr><td class="label">Nombre de pieces</td><td class="value">4.5</td><td class="label">Etat</td><td class="value">Bon etat</td></tr>
      <tr><td class="label">Surface parcelle m2</td><td class="value">0 m2</td><td class="label">Libre des le</td><td class="value">...</td></tr>
    </table>

    <div class="abs divider"></div>
    <div class="abs broker">
      <div class="broker-title">Votre courtier</div>
      <div class="broker-name">Claire Morand</div>
      <div class="broker-phone">0779876543</div>
    </div>
    <div class="abs portrait" role="img" aria-label="Portrait de la courtière"></div>

    <footer class="abs footer">
      <div class="col" style="left:18px">Norvelhaus Sàrl<br>Rue des Vignes 7<br>1804 Corsier</div>
      <div class="col contact" style="left:178px">info@norvelhaus.ch<br>www.norvelhaus.ch</div>
      <div class="col contact" style="left:392px">Fax. 021 555 40 10<br>Tél. 021 555 40 12</div>
    </footer>
  </section>

  <section class="page page-two">
    <svg class="abs header-band" width="548" height="236" viewBox="0 0 548 236">
      <polygon points="0,0 548,0 548,136 248,226 0,214" fill="#e95c57"/>
    </svg>
    <div class="abs title-box">
      <div class="title-main">Lumineux 4.5 de 100m2</div>
      <div class="title-sub">idéalement situé&nbsp; à 1200 Genève</div>
    </div>

    <div class="abs photo-bedroom" role="img" aria-label="Chambre avec grande armoire encastrée"></div>
    <div class="abs photo-bath" role="img" aria-label="Salle de bains"></div>
    <div class="abs photo-kitchen" role="img" aria-label="Cuisine ouverte"></div>
    <div class="abs photo-living" role="img" aria-label="Séjour lumineux avec parquet"></div>
    <div class="abs photo-terrace" role="img" aria-label="Balcon avec vue sur la verdure"></div>
    <div class="abs photo-garden" role="img" aria-label="Jardin arboré de la résidence"></div>

    <div class="abs location-box">Cet appartement<br>a l'avantage de se situer proche de toutes les commodités, à 3 minutes du Collège du Parc, à 1 minute de l'arrêt de bus et à 3 minutes des axes autoroutiers. Vous rejoindrez le centre-ville en 7 minutes. Des atouts que vous saurez apprécier.</div>

    <p class="abs intro">Venez découvrir sans attendre ce bel appartement situé dans un quartier calme et verdoyant, proche du centre-ville et de tous les commerces. Il offre de beaux volumes et des pièces de vie très lumineuses. Au 1er étage d'une copropriété soignée, c'est le bien idéal pour un couple ou une famille.</p>

    <div class="abs copy copy-a">
      <p>Cet appartement pourrait aussi convenir comme placement pour un client souhaitant le louer.</p>
      <p>Il est en bon état d'entretien et attend ses nouveaux propriétaires !</p>
      <p>Il se distribue ainsi :</p>
      <p>Une entrée avec armoire encastrée dessert d'une part la partie jour et d'autre part la partie nuit. Le spacieux séjour s'ouvre sur une cuisine entièrement équipée. Il profite d'une exposition idéale et d'un agréable balcon avec une belle vue dégagée sur la verdure.</p>
    </div>
    <div class="abs copy copy-b">
      <p>La partie nuit offre trois belles chambres, une salle de bains avec baignoire, lavabo, wc ainsi qu'un wc visiteurs.</p>
      <p>Deux places de parc intérieures en sus complètent ce bel appartement !</p>
      <p>N'hésitez pas, contactez-moi pour plus d'informations et pour une visite !</p>
    </div>
    <div class="abs price-tag">PRIX&nbsp; 895 000</div>

    <div class="abs cta">Pour plus d'informations contacter votre courtier<br><span class="cta-name">Claire Morand - 0779876543</span></div>

    <footer class="abs footer">
      <div class="col" style="left:10px">Norvelhaus Sàrl<br>Rue des Vignes 7<br>1804 Corsier</div>
      <div class="col" style="left:132px;top:20px">Fax. 021 555 40 10<br>Tél. 021 555 40 12</div>
      <div class="col" style="left:262px;top:20px">info@norvelhaus.ch<br>www.norvelhaus.ch</div>
      <div class="footer-brand">norvelhaus</div>
    </footer>
  </section>

</main>
</body>
</html>
```